Birchway Contracting website

I need a website for my construction. I want customers to see past builds and current projects Something that stands out and reflects awareness, safety, attention to details. I already have a logo designed by Studio Marrowfield
Target Market(s)
Residential and Commercial sectors
Industry/Entity Type
Construction
Logo Text
Birchway Contracting
Colors
EB3D1F
EC4F4E
F09395
F8D3D4
FCEDEE
Requirements
Must have
- My contact info
Nice to have
- Past projects

```html
<!DOCTYPE html>
<html lang="en">
<head>
<meta charset="utf-8">
<title>Birchway Contracting</title>
<link rel="stylesheet" href="https://fonts.googleapis.com/css2?family=Playfair+Display:wght@700;900&family=Open+Sans:wght@400;600;700&display=swap">
<style>
:root{
  --red:#EB3D1F;
  --coral:#EC4F4E;
  --rose:#F09395;
  --blush:#F8D3D4;
  --mist:#FCEDEE;
  --gold:#C8962E;
  --grey:#D9D9D9;
  --panel:#F4F4F4;
  --ink:#111111;
  --text:#555555;
  --white:#ffffff;
}
*{box-sizing:border-box;margin:0;padding:0}
html,body{width:1200px;height:4491px;overflow:hidden;background:var(--white)}
body{position:relative;font-family:"Open Sans",sans-serif;color:var(--ink)}
.abs{position:absolute}
.serif{font-family:"Playfair Display",serif;font-weight:900}
.btn{position:absolute;display:flex;align-items:center;justify-content:center;font-size:11px;font-weight:700;text-transform:uppercase;letter-spacing:.3px}
.btn-red{background:var(--red);color:var(--white)}
.btn-white{background:var(--white);color:var(--red)}
.btn-outline{border:1.5px solid var(--red);color:var(--red);background:var(--white)}

/* hero */
.hero{left:0;top:0;width:1200px;height:624px;background:linear-gradient(180deg,#2c2f36 0%,#4a4e55 40%,#3a3a34 75%,#22251f 100%)}
.hero-shade{left:0;top:0;width:1200px;height:624px;background:rgba(0,0,0,.25)}
.brand{display:flex;align-items:center;gap:6px;font-weight:700;font-size:12px;color:var(--white)}
.brand-mark{width:14px;height:14px;background:var(--red)}
.nav{left:415px;top:28px;display:flex;gap:27px;font-size:11px;font-weight:700;color:var(--white);text-transform:uppercase}
.nav .active{color:var(--red)}
.hero-title{left:0;width:1200px;top:205px;text-align:center;color:var(--white);font-size:58px;font-weight:700;font-family:"Playfair Display",serif}
.hero-sub{left:285px;width:630px;top:282px;text-align:center;color:#f0f0f0;font-size:15px;line-height:20px}

.section-title{font-size:40px;text-align:center;left:0;width:1200px}

/* about */
.about-photo{left:120px;top:741px;width:422px;height:368px;background:linear-gradient(135deg,#6aa0d8 0%,#9bbad6 35%,#b57a55 60%,#e4872a 85%,#d45c1c 100%)}
.about-text{left:609px;top:853px;width:470px;font-size:15px;line-height:24px;color:var(--text)}

/* bands */
.band{left:0;width:1200px;background:var(--grey)}
.frames{left:0;top:0}

/* services */
.card{position:absolute;background:var(--white);padding:0 20px}
.card.featured{background:var(--coral);color:var(--white)}
.card h3{font-family:"Playfair Display",serif;font-weight:700;font-size:14px;margin-top:80px}
.card p{font-size:11px;line-height:16px;color:var(--text);margin-top:14px}
.card.featured p{color:var(--white)}
.more{display:flex;align-items:center;gap:8px;font-size:10px;font-weight:700;color:var(--red);text-transform:uppercase;margin-top:24px}
.card.featured .more{color:var(--white)}
.icon{position:absolute;left:20px;top:18px}

/* projects */
.proj{position:absolute;top:2100px;width:231px;height:352px}
.proj-img{height:169px}
.proj-body{border-left:2px solid var(--gold);height:183px;padding:18px 6px 0 20px}
.proj-body h4{font-family:"Playfair Display",serif;font-weight:700;font-size:21px}
.proj-body p{font-size:11px;line-height:16px;color:var(--text);margin-top:10px}

/* testimonials */
.tcard{position:absolute;top:2817px;width:231px;height:240px;background:var(--white);text-align:center;padding:62px 24px 0}
.tcard h5{font-family:"Playfair Display",serif;font-weight:700;font-size:14px}
.tcard p{font-size:11px;line-height:16px;color:var(--text);margin-top:24px}
.stars{margin-top:14px;font-size:13px;letter-spacing:1px;color:var(--red)}
.stars .off{color:#bbb}
.avatar{position:absolute;top:-42px;left:74px;width:84px;height:84px;border-radius:50%}

/* contact */
.info-row{left:120px;display:flex;align-items:center;gap:14px;font-size:12px;font-weight:600}
.panel{left:542px;top:3397px;width:536px;height:463px;background:var(--panel)}
.field{position:absolute;background:var(--mist);font-size:11px;color:#444;padding:0 14px;display:flex;align-items:center}
.field.top{align-items:flex-start;padding-top:14px}
.label{font-size:11px;color:#444}

/* footer */
.footer{left:0;top:3985px;width:1200px;height:506px;background:#000}
.fcol{position:absolute;top:4172px;color:var(--white)}
.fcol h6{font-family:"Playfair Display",serif;font-weight:700;font-size:14px;text-transform:uppercase;letter-spacing:.3px}
.fcol ul{list-style:none;margin-top:24px;font-size:11px;line-height:33px;text-transform:uppercase}
.finfo{display:flex;gap:12px;align-items:flex-start;font-size:9px;line-height:14px;margin-top:22px}
.social{display:flex;flex-direction:column;gap:12px;margin-top:26px}
.social span{width:18px;height:18px;background:var(--white);border-radius:3px;display:block}
.copy{left:0;width:1200px;top:4460px;text-align:center;color:#ccc;font-size:11px}
</style>
</head>
<body>

<!-- hero -->
<div class="abs hero" role="img" aria-label="City skyline of tall towers along a river at dusk"></div>
<div class="abs hero-shade"></div>
<div class="abs brand" style="left:120px;top:27px"><span class="brand-mark"></span>Birchway Contracting</div>
<nav class="abs nav"><span class="active">Home</span><span>About</span><span>Services</span><span>Projects</span><span>Testimonials</span></nav>
<div class="btn btn-red" style="left:973px;top:21px;width:106px;height:31px">Contact Us</div>
<h1 class="abs hero-title">Build Your Dream house</h1>
<p class="abs hero-sub">Lorem ipsum dolor sit amet, consectetur adipiscing elit. Scelerisque eget feugiat dictumst ipsum vitae sed vestibulum.</p>
<div class="btn btn-red" style="left:488px;top:386px;width:106px;height:31px">Contact Us</div>
<div class="btn btn-white" style="left:609px;top:386px;width:106px;height:31px">Services</div>

<!-- grey bands -->
<div class="abs band" style="top:1235px;height:565px"></div>
<div class="abs band" style="top:2588px;height:565px"></div>

<!-- gold frames, above bands -->
<svg class="abs frames" width="1200" height="4491" viewBox="0 0 1200 4491" fill="none" stroke="#C8962E" stroke-width="2.5">
  <polygon points="100,1018 120,806 477,722 542,1028"/>
  <polygon points="64,810 98,1125 518,1125 518,1083"/>
  <polyline points="140,1166 550,1030"/>
  <polygon points="0,1352 1183,1165 1200,1718 14,1905"/>
  <polygon points="0,2703 1183,2517 1200,3070 14,3258"/>
  <polyline points="582,3397 582,3375 1116,3375 1116,3835 1078,3835"/>
  <polyline points="745,3375 1077,3325 1176,3795 1078,3816"/>
  <polyline points="1078,3816 650,3905 646,3880"/>
</svg>

<!-- about -->
<div class="abs about-photo" role="img" aria-label="Two site engineers in hard hats and high-visibility vests reviewing a construction site"></div>
<h2 class="abs serif" style="left:609px;top:780px;font-size:40px">About Us</h2>
<p class="abs about-text">Lorem ipsum dolor sit amet, consectetur adipiscing elit. Dolor eros eget parturient mauris, dignissim platea nibh auctor sapien. At orci, ornare leo praesent sed non, pulvinar. Eleifend viverra cras diam turpis nec nulla ut tellus tellus. Non duis aenean etiam nisl enim. Aliquam.</p>
<div class="btn btn-outline" style="left:605px;top:1029px;width:116px;height:30px">Learn More</div>

<!-- services -->
<h2 class="abs serif section-title" style="top:1295px">Our Services</h2>

<div class="card featured" style="left:120px;top:1413px;width:232px;height:280px">
  <svg class="icon" width="32" height="32" viewBox="0 0 32 32" fill="none" stroke="#fff" stroke-width="1.6"><rect x="2" y="4" width="28" height="24"/><path d="M2 10h28M2 16h28M2 22h28M10 4v6M20 4v6M6 10v6M16 10v6M26 10v6M10 16v6M20 16v6M6 22v6M16 22v6M26 22v6"/></svg>
  <h3>Architecture And Building</h3>
  <p>Lorem ipsum dolor sit amet, consectetur adipiscing elit. Dolor eros eget parturient mauris, dignissim platea nibh auctor sapien.</p>
  <div class="more">Read More <svg width="28" height="8" viewBox="0 0 28 8" fill="none" stroke="currentColor" stroke-width="1.4"><path d="M0 4h26M22 1l4 3-4 3"/></svg></div>
</div>
<div class="card" style="left:363px;top:1413px;width:232px;height:280px">
  <svg class="icon" width="28" height="28" viewBox="0 0 28 28" fill="none" stroke="#EB3D1F" stroke-width="1.6"><circle cx="14" cy="9" r="5"/><path d="M8 8h12M4 26v-4c0-4 4-6 10-6s10 2 10 6v4zM10 21h8"/></svg>
  <h3>Construction Consultants</h3>
  <p>Lorem ipsum dolor sit amet, consectetur adipiscing elit. Dolor eros eget parturient mauris, dignissim platea nibh auctor sapien.</p>
  <div class="more">Read More <svg width="28" height="8" viewBox="0 0 28 8" fill="none" stroke="currentColor" stroke-width="1.4"><path d="M0 4h26M22 1l4 3-4 3"/></svg></div>
</div>
<div class="card" style="left:605px;top:1413px;width:232px;height:280px">
  <svg class="icon" width="30" height="28" viewBox="0 0 30 28" fill="none" stroke="#EB3D1F" stroke-width="1.6"><rect x="2" y="4" width="22" height="22"/><circle cx="10" cy="13" r="3"/><path d="M5 23c1-4 9-4 10 0"/><circle cx="24" cy="6" r="4"/><path d="M18 18h4M18 22h4"/></svg>
  <h3>Construction Management</h3>
  <p>Lorem ipsum dolor sit amet, consectetur adipiscing elit. Dolor eros eget parturient mauris, dignissim platea nibh auctor sapien.</p>
  <div class="more">Read More <svg width="28" height="8" viewBox="0 0 28 8" fill="none" stroke="currentColor" stroke-width="1.4"><path d="M0 4h26M22 1l4 3-4 3"/></svg></div>
</div>
<div class="card" style="left:848px;top:1413px;width:231px;height:280px">
  <svg class="icon" width="30" height="30" viewBox="0 0 30 30" fill="none" stroke="#EB3D1F" stroke-width="1.6"><path d="M2 28h26M5 28V16l8-4v16M13 28V8l12-6v26M17 10h4M17 15h4M17 20h4M8 19h2M8 23h2"/></svg>
  <h3>Design Build Contracts</h3>
  <p>Lorem ipsum dolor sit amet, consectetur adipiscing elit. Dolor eros eget parturient mauris, dignissim platea nibh auctor sapien.</p>
  <div class="more">Read More <svg width="28" height="8" viewBox="0 0 28 8" fill="none" stroke="currentColor" stroke-width="1.4"><path d="M0 4h26M22 1l4 3-4 3"/></svg></div>
</div>

<!-- projects -->
<h2 class="abs serif section-title" style="top:1973px">Our Projects</h2>
<svg class="abs" style="left:62px;top:2269px" width="16" height="24" viewBox="0 0 16 24" fill="none" stroke="#111" stroke-width="3"><path d="M12 2 3 12l9 10"/></svg>
<svg class="abs" style="left:1118px;top:2269px" width="16" height="24" viewBox="0 0 16 24" fill="none" stroke="#111" stroke-width="3"><path d="M4 2l9 10-9 10"/></svg>

<div class="proj" style="left:120px">
  <div class="proj-img" role="img" aria-label="Large white family house on a green lawn" style="background:linear-gradient(180deg,#a9c8e6 0%,#dfe6ea 45%,#6e8f4a 75%,#4f7233 100%)"></div>
  <div class="proj-body"><h4>Project 1</h4><p>Lorem ipsum dolor sit amet, consectetur adipiscing elit. Dictum erat lorem fermentum lectus volutpat.</p>
  <div class="more">Read More <svg width="28" height="8" viewBox="0 0 28 8" fill="none" stroke="currentColor" stroke-width="1.4"><path d="M0 4h26M22 1l4 3-4 3"/></svg></div></div>
</div>
<div class="proj" style="left:363px">
  <div class="proj-img" role="img" aria-label="Modern white villa with a turquoise pool and palm trees" style="background:linear-gradient(180deg,#cfe3ef 0%,#eef2f2 45%,#7bc8c8 80%,#4aa6ad 100%)"></div>
  <div class="proj-body"><h4>Project 1</h4><p>Lorem ipsum dolor sit amet, consectetur adipiscing elit. Dictum erat lorem fermentum lectus volutpat.</p>
  <div class="more">Read More <svg width="28" height="8" viewBox="0 0 28 8" fill="none" stroke="currentColor" stroke-width="1.4"><path d="M0 4h26M22 1l4 3-4 3"/></svg></div></div>
</div>
<div class="proj" style="left:605px">
  <div class="proj-img" role="img" aria-label="Bright living room with a tan leather sofa" style="background:linear-gradient(180deg,#e9ecea 0%,#b9c3bd 45%,#b27a4f 75%,#d9d6d0 100%)"></div>
  <div class="proj-body"><h4>Project 1</h4><p>Lorem ipsum dolor sit amet, consectetur adipiscing elit. Dictum erat lorem fermentum lectus volutpat.</p>
  <div class="more">Read More <svg width="28" height="8" viewBox="0 0 28 8" fill="none" stroke="currentColor" stroke-width="1.4"><path d="M0 4h26M22 1l4 3-4 3"/></svg></div></div>
</div>
<div class="proj" style="left:848px">
  <div class="proj-img" role="img" aria-label="Apartment block with a red facade and balconies" style="background:linear-gradient(180deg,#d8232a 0%,#c9302c 35%,#8a8a8a 60%,#5c5c5c 100%)"></div>
  <div class="proj-body"><h4>Project 1</h4><p>Lorem ipsum dolor sit amet, consectetur adipiscing elit. Dictum erat lorem fermentum lectus volutpat.</p>
  <div class="more">Read More <svg width="28" height="8" viewBox="0 0 28 8" fill="none" stroke="currentColor" stroke-width="1.4"><path d="M0 4h26M22 1l4 3-4 3"/></svg></div></div>
</div>

<!-- testimonials -->
<h2 class="abs serif section-title" style="top:2660px">Testimonials</h2>

<div class="tcard" style="left:120px"><div class="avatar" role="img" aria-label="Customer portrait" style="background:linear-gradient(180deg,#6fc0d6,#2e5d6e)"></div><h5>Full Name</h5><p>Lorem ipsum dolor sit amet, consectetur adipiscing elit. Morbi hendrerit ultrices risus dolor accumsan magna. Fringilla lacinia ut lorem egestas.</p><div class="stars">★★★★★</div></div>
<div class="tcard" style="left:363px"><div class="avatar" role="img" aria-label="Customer portrait" style="background:linear-gradient(180deg,#c9a27a,#7d5a3e)"></div><h5>Full Name</h5><p>Lorem ipsum dolor sit amet, consectetur adipiscing elit. Morbi hendrerit ultrices risus dolor accumsan magna. Fringilla lacinia ut lorem egestas.</p><div class="stars">★★★★<span class="off">★</span></div></div>
<div class="tcard" style="left:605px"><div class="avatar" role="img" aria-label="Customer portrait" style="background:linear-gradient(180deg,#9a9a9a,#5a5a5a)"></div><h5>Full Name</h5><p>Lorem ipsum dolor sit amet, consectetur adipiscing elit. Morbi hendrerit ultrices risus dolor accumsan magna. Fringilla lacinia ut lorem egestas.</p><div class="stars">★★★<span class="off">★★</span></div></div>
<div class="tcard" style="left:848px"><div class="avatar" role="img" aria-label="Customer portrait" style="background:linear-gradient(180deg,#e8e2dc,#3a2a22)"></div><h5>Full Name</h5><p>Lorem ipsum dolor sit amet, consectetur adipiscing elit. Morbi hendrerit ultrices risus dolor accumsan magna. Fringilla lacinia ut lorem egestas.</p><div class="stars">★★★★★</div></div>

<!-- contact -->
<h2 class="abs serif" style="left:120px;top:3400px;font-size:40px">Contact Us</h2>
<div class="abs info-row" style="top:3541px">
  <svg width="20" height="24" viewBox="0 0 20 24" fill="#C8962E"><path d="M10 0C4.5 0 0 4.3 0 9.6 0 16 10 24 10 24s10-8 10-14.4C20 4.3 15.5 0 10 0zm0 13a3.5 3.5 0 1 1 0-7 3.5 3.5 0 0 1 0 7z"/></svg>
  14 Harbour Row, Eastvale, ON K7P 4M2
</div>
<div class="abs info-row" style="top:3610px">
  <svg width="24" height="24" viewBox="0 0 24 24" fill="#C8962E"><path d="M6.6 10.8a15 15 0 0 0 6.6 6.6l2.2-2.2c.3-.3.7-.4 1-.2 1.1.4 2.3.6 3.6.6.6 0 1 .4 1 1V20c0 .6-.4 1-1 1A17 17 0 0 1 3 4c0-.6.4-1 1-1h3.5c.6 0 1 .4 1 1 0 1.3.2 2.5.6 3.6.1.3 0 .7-.2 1z"/></svg>
  +1 555-010-0000
</div>
<div class="abs info-row" style="top:3678px">
  <svg width="26" height="20" viewBox="0 0 26 20" fill="none" stroke="#C8962E" stroke-width="2"><rect x="1" y="1" width="24" height="18" rx="2"/><path d="M1 3l12 9 12-9"/></svg>
  hello@birchwaybuild.com
</div>

<div class="abs panel"></div>
<div class="abs label" style="left:581px;top:3466px">First Name</div>
<div class="field" style="left:581px;top:3486px;width:209px;height:37px;border:1.5px solid var(--red);background:var(--white)">|</div>
<div class="field" style="left:828px;top:3486px;width:211px;height:37px">Last Name</div>
<div class="field" style="left:581px;top:3553px;width:458px;height:37px">Email Address</div>
<div class="field top" style="left:581px;top:3621px;width:458px;height:111px">Message</div>
<div class="btn btn-red" style="left:581px;top:3753px;width:115px;height:30px;font-size:12px;text-transform:none">Send</div>

<!-- footer -->
<footer class="abs footer"></footer>
<div class="abs brand" style="left:120px;top:4060px;font-size:13px"><span class="brand-mark"></span>Birchway Contracting</div>
<div class="fcol" style="left:120px"><h6>Quick Links</h6><ul><li>Home</li><li>About</li><li>Services</li><li>Projects</li><li>Testimonials</li></ul></div>
<div class="fcol" style="left:363px"><h6>Contact Info</h6>
  <div class="finfo"><svg width="16" height="20" viewBox="0 0 20 24" fill="#C8962E"><path d="M10 0C4.5 0 0 4.3 0 9.6 0 16 10 24 10 24s10-8 10-14.4C20 4.3 15.5 0 10 0zm0 13a3.5 3.5 0 1 1 0-7 3.5 3.5 0 0 1 0 7z"/></svg><span>14 Harbour Row, Eastvale,<br>ON K7P 4M2</span></div>
  <div class="finfo"><svg width="20" height="20" viewBox="0 0 24 24" fill="#C8962E"><path d="M6.6 10.8a15 15 0 0 0 6.6 6.6l2.2-2.2c.3-.3.7-.4 1-.2 1.1.4 2.3.6 3.6.6.6 0 1 .4 1 1V20c0 .6-.4 1-1 1A17 17 0 0 1 3 4c0-.6.4-1 1-1h3.5c.6 0 1 .4 1 1 0 1.3.2 2.5.6 3.6.1.3 0 .7-.2 1z"/></svg><span>+1 555-010-0000</span></div>
  <div class="finfo"><svg width="22" height="16" viewBox="0 0 26 20" fill="none" stroke="#C8962E" stroke-width="2"><rect x="1" y="1" width="24" height="18" rx="2"/><path d="M1 3l12 9 12-9"/></svg><span>hello@birchwaybuild.com</span></div>
</div>
<div class="fcol" style="left:657px"><h6>Legal</h6><ul><li>Privacy Policy</li><li>Refund and Returns</li></ul></div>
<div class="fcol" style="left:950px"><h6>Social Links</h6><div class="social"><span aria-label="Social profile"></span><span aria-label="Social profile"></span><span aria-label="Social profile"></span></div></div>
<div class="abs copy">Copyright © 2022 | All rights reserved by CONSTRUCTION</div>

</body>
</html>
```